Brightmere Business Card Redesign & Logo Update

We need to update our business cards to something more modern and fresh. Brightmere can provide the current color schemes and old design examples, but welcome creativity in helping us with this redesign. PLEASE NOTE that we no longer utilize the "tree" and/or "leaf" imagery in our branding. If able would apprecaite an update on the quality of our "words only" logo in Ai. / PNG formats too.

Target Market(s)

Investors, landowners, corporate partners, contractors

Industry/Entity Type

Environmental Restoration & Conservation

Contact Information for Business Card

Logo, persons name, title, mailing address, phone and email, website url

Font styles to use
Other font styles liked:
• Merriweather

Requirements
Nice to have
• Logo, persons name, title, mailing address, phone and email, website url, but open to ideams
Should not have
• No all back backgrounds

```html
<!DOCTYPE html>
<html lang="en">
<head>
<meta charset="utf-8">
<title>Brightmere Business Card</title>
<link rel="stylesheet" href="https://fonts.googleapis.com/css2?family=Bebas+Neue&family=Merriweather:wght@400&display=swap">
<style>
  :root {
    --orange: #ee7d22;
    --green: #157a40;
    --ink: #111111;
    --paper: #ffffff;
    --backdrop: #e8e5e0;
    --body-text: #2a2a2a;
  }
  * { margin: 0; padding: 0; box-sizing: border-box; }
  html, body { width: 900px; height: 1200px; overflow: hidden; }
  body { background: var(--backdrop); position: relative; font-family: "Merriweather", Georgia, serif; }

  .card {
    position: absolute; left: 67px; width: 763px; height: 446px;
    border-radius: 30px; overflow: hidden;
  }
  .card--front { top: 107px; background: var(--paper); }
  .card--back { top: 647px; background: var(--green); }

  .display { font-family: "Bebas Neue", "Oswald", sans-serif; font-weight: 400; line-height: 1; }

  /* Front */
  .accent-tab { position: absolute; left: 0; top: 79px; width: 21px; height: 64px; background: var(--orange); }
  .person { position: absolute; left: 46px; top: 78px; }
  .person__name { font-size: 44px; letter-spacing: 0.5px; }
  .person__first { color: var(--orange); }
  .person__last { color: var(--green); }
  .person__title { font-size: 27px; color: var(--ink); margin-top: 2px; }

  .brand--front { position: absolute; right: 44px; top: 52px; text-align: right; }
  .brand__name { color: var(--green); font-size: 80px; letter-spacing: 1px; }
  .brand__tagline { color: var(--ink); font-size: 25px; margin-top: -4px; }

  .divider { position: absolute; top: 281px; height: 4px; }
  .divider--orange { left: 46px; width: 335px; background: var(--orange); }
  .divider--green { left: 386px; width: 333px; height: 2px; top: 284px; background: var(--green); }

  .contact { position: absolute; left: 46px; top: 302px; list-style: none; }
  .contact__item { display: flex; align-items: center; height: 26px; font-size: 16.5px; color: var(--body-text); }
  .contact__icon { width: 16px; height: 16px; margin: 0 13px 0 2px; fill: var(--orange); }

  .address { position: absolute; right: 44px; top: 302px; text-align: right; font-style: normal; font-size: 16.5px; line-height: 26px; color: var(--body-text); }

  .base-band { position: absolute; left: 0; bottom: 0; height: 20px; }
  .base-band--orange { width: 383px; background: var(--orange); }
  .base-band--green { left: 383px; right: 0; background: var(--green); }

  /* Back */
  .brand--back { position: absolute; left: 0; right: 0; top: 152px; text-align: center; }
  .brand--back .brand__name { color: var(--paper); font-size: 122px; letter-spacing: 2px; }
  .brand--back .brand__tagline { font-size: 38px; margin-top: -6px; }
  .back-url { position: absolute; left: 0; right: 0; top: 390px; text-align: center; color: var(--paper); font-size: 23px; letter-spacing: 1.5px; }
</style>
</head>
<body>

<section class="card card--front" aria-label="Business card front">
  <div class="accent-tab"></div>
  <div class="person">
    <div class="person__name display"><span class="person__first">Daniel</span> <span class="person__last">Hart</span></div>
    <div class="person__title display">Managing Director</div>
  </div>

  <div class="brand brand--front">
    <div class="brand__name display">BRIGHTMERE</div>
    <div class="brand__tagline display">Environmental Credit Company</div>
  </div>

  <div class="divider divider--orange"></div>
  <div class="divider divider--green"></div>

  <ul class="contact">
    <li class="contact__item">
      <svg class="contact__icon" viewBox="0 0 24 24" aria-hidden="true"><path d="M6.6 10.8c1.4 2.8 3.8 5.1 6.6 6.6l2.2-2.2c.3-.3.7-.4 1-.2 1.1.4 2.3.6 3.6.6.6 0 1 .4 1 1V20c0 .6-.4 1-1 1C10.6 21 3 13.4 3 4c0-.6.4-1 1-1h3.5c.6 0 1 .4 1 1 0 1.3.2 2.5.6 3.6.1.3 0 .7-.2 1l-2.3 2.2z"/></svg>
      555-318-4720
    </li>
    <li class="contact__item">
      <svg class="contact__icon" viewBox="0 0 24 24" aria-hidden="true"><path d="M2 5h20v14H2z M2 5l10 8 10-8" fill="var(--orange)" stroke="#fff" stroke-width="1.5"/></svg>
      Daniel@emailaddress.com
    </li>
    <li class="contact__item">
      <svg class="contact__icon" viewBox="0 0 24 24" aria-hidden="true"><circle cx="12" cy="12" r="10"/><path d="M2 12h20M12 2c3 3 3 17 0 20M12 2c-3 3-3 17 0 20M4 7h16M4 17h16" stroke="#fff" stroke-width="1.4" fill="none"/></svg>
      www.yourwebsitehere.com
    </li>
  </ul>

  <address class="address">
    118 Harlow Street NE<br>
    Suite 210, Easton Falls<br>
    MI 49021
  </address>

  <div class="base-band base-band--orange"></div>
  <div class="base-band base-band--green"></div>
</section>

<section class="card card--back" aria-label="Business card back">
  <div class="brand brand--back">
    <div class="brand__name display">BRIGHTMERE</div>
    <div class="brand__tagline display">Environmental Credit Company</div>
  </div>
  <div class="back-url display">www.yourwebsitehere.com</div>
</section>

</body>
</html>
```